Brightwell Pipeworks

We need a webpage designed for http://www.brightwellpipeworks.example/. Something clean, and focused.

Homepage needs some call to action at the top, also this is a local business so things like telephone, address, ratings, social media, should be present.

We like contact forms above the fold.

http://www.ravodinplumbing.example/ is a website that was referenced, although I personally think it looks "old". Something more modern.

http://www.tedsplumbing.example/ has the pieces we like, bit is not visually appealing.

http://mintwashcrewok.example/ is nice looking but doesnt have a good call to action

http://www.lanterly.example/ and http://www.theneighborpass.example/ is great

Target Market(s)

Adluts, homeowners

Industry/Entity Type

Business

Font styles to use
Sans Serif

Requirements
Must have
• Homepage needs some call to action form at the top, also this is a local business so things like telephone, address, ratings, social media,
Nice to have
• Prefer layouts that have a fixed max width - not that stretch off the screen
Should not have
• don't overdo "plumber theme" - we want professional, clean and uncluttered. No generic pictures of "plumbers" or cartoon plumbers.

```html
<!DOCTYPE html>
<html lang="en">
<head>
<meta charset="utf-8">
<title>Brightwell Pipeworks</title>
<link href="https://fonts.googleapis.com/css2?family=Open+Sans:wght@400;600&display=swap" rel="stylesheet">
<style>
:root{
  --blue:#2f6fc8;
  --blue-text:#2467c0;
  --nav-dark:#3b3b3b;
  --grey-band:#e9e9e9;
  --light-band:#f3f3f3;
  --footer:#323232;
  --text:#333;
  --muted:#666;
  --box-bg:#eef3fb;
  --box-border:#c8d7ee;
}
*{box-sizing:border-box;margin:0;padding:0}
html,body{width:932px;height:1200px;overflow:hidden;background:#fff}
body{position:relative;font-family:'Open Sans',sans-serif;color:var(--text)}
.abs{position:absolute}
/* header */
.brand{left:78px;top:24px;display:flex;align-items:center;gap:8px;font-size:21px;font-weight:600;color:var(--blue-text)}
.brand-dot{width:28px;height:28px;border-radius:50%;background:var(--blue)}
.call{right:112px;top:22px;text-align:right}
.call small{display:block;font-size:13px;color:#555}
.call strong{display:block;font-size:16px;font-weight:400;color:var(--blue-text)}
.call-icon{left:830px;top:26px}
/* nav */
.nav{left:0;top:81px;width:932px;height:35px;background:var(--blue)}
.nav ul{list-style:none;position:absolute;left:77px;top:0;display:flex;height:35px}
.nav li{height:35px;line-height:35px;text-align:center;color:#fff;font-size:10.5px;border-right:1px solid #2a62b2}
.nav li.active{background:var(--nav-dark)}
/* hero */
.hero{left:0;top:116px;width:932px;height:318px;background:linear-gradient(180deg,#b9c0b8 0%,#8f958f 45%,#5e665f 100%)}
.hero-arrow{top:261px;width:29px;height:29px;background:#e8e8e8;display:flex;align-items:center;justify-content:center}
.caption{left:256px;top:380px;width:421px;height:35px;background:rgba(0,0,0,.78);color:#fff;font-size:19px;text-align:center;line-height:35px}
/* quick contact */
.quick{left:0;top:434px;width:932px;height:94px;background:var(--grey-band)}
.quick h2{position:absolute;top:12px;width:100%;text-align:center;font-weight:400;font-size:20px;color:var(--blue-text)}
.field{position:absolute;top:47px;height:29px;background:#fff;border:1px solid #ddd;font-size:10.5px;color:#888;padding:7px 10px}
.quick-btn{position:absolute;left:748px;top:47px;width:83px;height:29px;background:var(--blue);color:#fff;font-size:10.5px;text-align:center;line-height:29px}
/* intro */
.intro{left:95px;top:556px;width:742px;text-align:center;font-size:13px;line-height:21px;color:var(--muted)}
.area{left:87px;top:618px;font-size:13px;line-height:21px;color:var(--blue-text)}
.points{left:87px;top:670px;list-style:none}
.points li{font-size:13px;height:26px;display:flex;align-items:center;gap:9px}
.video{left:594px;top:624px;width:250px;height:141px;background:linear-gradient(90deg,#6a4f3c,#b99b85 55%,#d6c8c0)}
.play{position:absolute;left:104px;top:55px;width:42px;height:30px;border-radius:6px;background:#1c1c1c;display:flex;align-items:center;justify-content:center}
/* services */
.services{left:77px;top:795px;width:777px;height:106px;background:var(--box-bg);border:1px solid var(--box-border)}
.svc{position:absolute;list-style:none;top:18px}
.svc li{font-size:13px;color:var(--blue-text);height:24px;display:flex;align-items:center;gap:7px}
/* badges */
.badge{position:absolute}
.dealer{left:115px;top:937px;width:90px;height:70px;border-radius:50%;background:#2d76c4}
.bbb{left:257px;top:939px;width:121px;height:46px;border-radius:5px;background:#0e5a8a}
.bbb-note{left:255px;top:993px;font-size:7.5px;color:var(--blue-text)}
.reviews{left:437px;top:938px;width:101px;height:45px;border:2px solid #c21b17;background:#d32323}
.reviews-note{left:437px;top:991px;font-size:11.5px;line-height:15px;color:var(--blue-text)}
.social-badge{top:936px;width:104px;height:27px;border:1px solid #ccc;background:#e9edf3}
/* contact strip */
.strip{left:0;top:1046px;width:932px;height:74px;background:var(--light-band)}
.strip-item{position:absolute;top:28px;display:flex;align-items:center;gap:10px;font-size:10.5px;color:#666}
/* footer */
.footer{left:0;top:1120px;width:932px;height:80px;background:var(--footer)}
.footer-links{position:absolute;left:78px;top:17px;font-size:10.5px;color:#ddd;word-spacing:2px}
.footer-links span{color:#999;margin:0 8px}
.copy{position:absolute;left:78px;top:46px;font-size:10px;color:#ccc}
.footer-social{position:absolute;left:751px;top:29px;display:flex;gap:8px}
.footer-social i{width:19px;height:19px;border-radius:50%;background:#6d6d6d;display:block}
</style>
</head>
<body>

<div class="abs brand"><span class="brand-dot"></span>Brightwell Pipeworks</div>
<div class="abs call"><small>Call Today</small><strong>626-555-0148</strong></div>
<svg class="abs call-icon" width="24" height="24" viewBox="0 0 24 24"><path d="M4 3c2-1 4 0 5 2l1 3-2 2c1 3 3 5 6 6l2-2 3 1c2 1 3 3 2 5" fill="none" stroke="var(--blue)" stroke-width="4" stroke-linecap="round"/></svg>

<nav class="abs nav"><ul>
  <li class="active" style="width:89px">HOME</li>
  <li style="width:107px">ABOUT US</li>
  <li style="width:99px">SERVICES</li>
  <li style="width:108px">PRODUCTS</li>
  <li style="width:127px">SERVICE AREAS</li>
  <li style="width:127px">TESTIMONIALS</li>
  <li style="width:121px">CONTACT US</li>
</ul></nav>

<div class="abs hero" role="img" aria-label="Photo of the service team standing in front of company vans"></div>
<div class="abs hero-arrow" style="left:0"><svg width="14" height="14" viewBox="0 0 14 14"><path d="M10 1L3 7l7 6" fill="none" stroke="#444" stroke-width="3"/></svg></div>
<div class="abs hero-arrow" style="left:903px"><svg width="14" height="14" viewBox="0 0 14 14"><path d="M4 1l7 6-7 6" fill="none" stroke="#444" stroke-width="3"/></svg></div>
<div class="abs caption">Duis ultricies tortor vitae enim fermentum</div>

<section class="abs quick">
  <h2>Quick Contact</h2>
  <div class="field" style="left:100px;width:141px">Name</div>
  <div class="field" style="left:246px;width:141px">E-mail</div>
  <div class="field" style="left:392px;width:141px">Phone</div>
  <div class="field" style="left:537px;width:206px">Address</div>
  <div class="quick-btn">CONTACT US</div>
</section>

<p class="abs intro">Brightwell Pipeworks is the Sole Authorized Dealer and Installer for Clearbrook Water Systems in Orange County, Riverside and San Bernardino Counties, and San Gabriel Valley, Southeast Los Angeles.</p>

<p class="abs area">Plumbers with a Service Area from Burbank to Ontario, all of Orange County,<br>From Seal Beach to Laguna Beach, Anaheim and Corona, All Points In-Between</p>

<ul class="abs points">
  <li><svg width="8" height="10" viewBox="0 0 8 10"><path d="M2 1l4 4-4 4" fill="none" stroke="#333" stroke-width="2"/></svg>You approve the price before we start work.</li>
  <li><svg width="8" height="10" viewBox="0 0 8 10"><path d="M2 1l4 4-4 4" fill="none" stroke="#333" stroke-width="2"/></svg>Same-day service generally available.</li>
  <li><svg width="8" height="10" viewBox="0 0 8 10"><path d="M2 1l4 4-4 4" fill="none" stroke="#333" stroke-width="2"/></svg>Always FREE work estimates.</li>
  <li><svg width="8" height="10" viewBox="0 0 8 10"><path d="M2 1l4 4-4 4" fill="none" stroke="#333" stroke-width="2"/></svg>Call today to find out how we can help!</li>
</ul>

<div class="abs video" role="img" aria-label="Introductory video of the company owner speaking in a kitchen">
  <div class="play"><svg width="12" height="12" viewBox="0 0 12 12"><path d="M2 1l9 5-9 5z" fill="#fff"/></svg></div>
</div>

<section class="abs services">
  <ul class="svc" style="left:26px">
    <li><svg width="11" height="9" viewBox="0 0 11 9"><path d="M1 5l3 3 6-7" fill="none" stroke="var(--blue)" stroke-width="1.6"/></svg>Trenchless Sewer Repair</li>
    <li><svg width="11" height="9" viewBox="0 0 11 9"><path d="M1 5l3 3 6-7" fill="none" stroke="var(--blue)" stroke-width="1.6"/></svg>Sewer Pipe Bursting Repair</li>
    <li><svg width="11" height="9" viewBox="0 0 11 9"><path d="M1 5l3 3 6-7" fill="none" stroke="var(--blue)" stroke-width="1.6"/></svg>Video Pipe Inspections</li>
  </ul>
  <ul class="svc" style="left:285px">
    <li><svg width="11" height="9" viewBox="0 0 11 9"><path d="M1 5l3 3 6-7" fill="none" stroke="var(--blue)" stroke-width="1.6"/></svg>Sewer &amp; Drain Hydro-Jetting</li>
    <li><svg width="11" height="9" viewBox="0 0 11 9"><path d="M1 5l3 3 6-7" fill="none" stroke="var(--blue)" stroke-width="1.6"/></svg>Orangeburg Pipes</li>
    <li><svg width="11" height="9" viewBox="0 0 11 9"><path d="M1 5l3 3 6-7" fill="none" stroke="var(--blue)" stroke-width="1.6"/></svg>Water &amp; Gas Leak Detection</li>
  </ul>
  <ul class="svc" style="left:545px">
    <li><svg width="11" height="9" viewBox="0 0 11 9"><path d="M1 5l3 3 6-7" fill="none" stroke="var(--blue)" stroke-width="1.6"/></svg>Copper &amp; PEX Tubing Repipes</li>
    <li><svg width="11" height="9" viewBox="0 0 11 9"><path d="M1 5l3 3 6-7" fill="none" stroke="var(--blue)" stroke-width="1.6"/></svg>Tankless Water Heaters</li>
    <li><svg width="11" height="9" viewBox="0 0 11 9"><path d="M1 5l3 3 6-7" fill="none" stroke="var(--blue)" stroke-width="1.6"/></svg>Clearbrook Water Filters</li>
  </ul>
</section>

<div class="badge dealer" role="img" aria-label="Authorized dealer badge"></div>
<div class="badge bbb" role="img" aria-label="Accredited business badge"></div>
<div class="abs bbb-note">CLICK TO VERIFY OUR A+ RATING!</div>
<div class="badge reviews" role="img" aria-label="Five-star reviews badge"></div>
<div class="abs reviews-note">Please Feel Free To<br>Click and Check our Reviews!</div>
<div class="badge social-badge" style="left:602px" role="img" aria-label="Social page badge"></div>
<div class="badge social-badge" style="left:716px" role="img" aria-label="Social feed badge"></div>

<section class="abs strip">
  <div class="strip-item" style="left:86px">
    <svg width="18" height="20" viewBox="0 0 18 20"><rect x="1" y="2" width="16" height="17" fill="none" stroke="#999" stroke-width="2"/><path d="M6 2v10l3-2 3 2V2" fill="#999"/></svg>
    Brightwell Pipeworks, 418 West Marlow Place, Covina, CA&nbsp; 91723
  </div>
  <div class="strip-item" style="left:447px">
    <svg width="22" height="22" viewBox="0 0 24 24"><path d="M4 3c2-1 4 0 5 2l1 3-2 2c1 3 3 5 6 6l2-2 3 1c2 1 3 3 2 5" fill="none" stroke="#999" stroke-width="4" stroke-linecap="round"/></svg>
    Phone: (626) 555-0148
  </div>
  <div class="strip-item" style="left:636px">
    <svg width="21" height="15" viewBox="0 0 21 15"><rect x="0" y="0" width="21" height="15" fill="#aaa"/><path d="M0 0l10.5 8L21 0" fill="none" stroke="#f3f3f3" stroke-width="1.5"/></svg>
    E-mail : info@brightwellpipeworks.example
  </div>
</section>

<footer class="abs footer">
  <div class="footer-links">Home<span>|</span>About us<span>|</span>Services<span>|</span>Products<span>|</span>Service Areas<span>|</span>Testimonials<span>|</span>Contact us</div>
  <div class="copy">Copyright &copy; 2014 Brightwell Pipeworks. All rights reserved.</div>
  <div class="footer-social"><i></i><i></i><i></i><i></i></div>
</footer>

</body>
</html>
```